TKRV Restaurant Group Take Out Bags

We need bags designed for our restaurant group.

We are an upscale Chinese food restaurant. I have uploaded a few photos that our boss liked as inspiration. I also uploaded a few of our menus so you can see the aesthetic and our logos.

The main focus is TKRV Group, but please have all 5 logos somewhere on the bag.

Red, black and gold are the ideal color focus.

Two bag sizes, but they can have the same design.
Large: 15"W, 15"H, 8"D; Small: 10"W, 12"H, 6"D

Industry/Entity Type

Restaurant

```html
<!DOCTYPE html>
<html lang="en">
<head>
<meta charset="utf-8">
<title>TKRV Group Take Out Bags</title>
<link rel="stylesheet" href="https://fonts.googleapis.com/css2?family=Rosario:wght@500;700&family=Montserrat:wght@600;800&family=Marcellus&display=swap">
<style>
  :root {
    --backdrop: #d3a675;
    --paper: #ffffff;
    --red: #c41a22;
    --gold: #a1772a;
    --ink: #1e1e1e;
    --white: #ffffff;
  }
  * { margin: 0; padding: 0; box-sizing: border-box; }
  html, body { width: 700px; height: 1200px; overflow: hidden; background: var(--backdrop); }
  .sheet { position: relative; width: 700px; height: 1200px; }
  .bag-panel { position: absolute; left: 100px; display: block; background: var(--paper); box-shadow: 0 3px 8px rgba(0,0,0,0.18); }
  .bag-panel--large { top: 40px; width: 500px; height: 500px; }
  .bag-panel--small { top: 570px; width: 500px; height: 600px; }
  .panel-paper { fill: var(--paper); }
  .gold-field { fill: var(--gold); }
  .red-band { fill: var(--red); }
  .brand-square { fill: var(--gold); }
  .brand-name { font-family: "Marcellus", serif; fill: var(--ink); }
  .brand-sub { font-family: "Montserrat", sans-serif; font-weight: 600; fill: var(--ink); }
  .headline { font-family: "Rosario", sans-serif; font-weight: 700; fill: var(--white); }
  .headline--small { font-weight: 500; }
  .tagline { font-family: "Montserrat", sans-serif; font-weight: 800; fill: var(--ink); }
  .venue-name, .venue-line { font-family: "Montserrat", sans-serif; font-weight: 600; }
  .venue--lark { fill: var(--gold); }
  .venue--lantern { fill: var(--red); }
  .venue--harbor { fill: var(--ink); }
</style>
</head>
<body>
<main class="sheet">

  <!-- Large bag: 15 x 15 -->
  <svg class="bag-panel bag-panel--large" viewBox="0 0 632 632" aria-label="Large bag face">
    <rect class="panel-paper" width="632" height="632"/>
    <polygon class="gold-field" role="img" aria-label="Large gold geometric brand decoration" points="269,328 632,-35 632,483 539,576"/>
    <polygon class="red-band" points="0,208 352,208 258,318 366,423 0,423"/>

    <rect class="brand-square" x="133" y="62" width="44" height="44"/>
    <text class="brand-name" x="155" y="164" text-anchor="middle" font-size="34" letter-spacing="3">TKRV</text>
    <text class="brand-sub" x="155" y="180" text-anchor="middle" font-size="7" letter-spacing="9">GROUP</text>

    <text class="headline" x="155" y="296" text-anchor="middle" font-size="88" letter-spacing="-3">TOP</text>
    <text class="headline" x="155" y="343" text-anchor="middle" font-size="44">QUALITY</text>
    <text class="headline" x="155" y="381" text-anchor="middle" font-size="30">RESTAURANT</text>
    <text class="headline headline--small" x="155" y="403" text-anchor="middle" font-size="16">MANAGEMENT</text>

    <text class="tagline" x="67" y="455" font-size="16.5" letter-spacing="0.5">WITH YEARS OF EXPERIENCE</text>
    <text class="tagline" x="67" y="473" font-size="16.5" letter-spacing="0.5">AND EXCELLENCE</text>

    <g class="venue--lark">
      <rect x="98" y="520" width="16" height="16"/>
      <text class="venue-name" x="106" y="558" text-anchor="middle" font-size="13">THE LARK</text>
      <text class="venue-line" x="106" y="567" text-anchor="middle" font-size="5.5">WHISKEY &amp; COFFEE</text>
    </g>
    <g class="venue--lantern">
      <circle cx="221" cy="528" r="8"/>
      <text class="venue-name" x="221" y="552" text-anchor="middle" font-size="12">JADE LANTERN</text>
      <text class="venue-line" x="221" y="561" text-anchor="middle" font-size="4.5">BAYVIEW | ELMWOOD | STONE RIDGE</text>
      <text class="venue-line" x="221" y="575" text-anchor="middle" font-size="4.5">JADELANTERNDINING.COM</text>
    </g>
    <g class="venue--harbor">
      <circle cx="353" cy="528" r="8"/>
      <text class="venue-name" x="353" y="556" text-anchor="middle" font-size="15">HARBOR</text>
      <text class="venue-line" x="353" y="565" text-anchor="middle" font-size="6" letter-spacing="3">PETE'S</text>
    </g>
  </svg>

  <!-- Small bag: 10 x 12 -->
  <svg class="bag-panel bag-panel--small" viewBox="0 0 629 755" aria-label="Small bag face">
    <rect class="panel-paper" width="629" height="755"/>
    <polygon class="gold-field" role="img" aria-label="Large gold geometric brand decoration" points="276,393 629,40 629,585 581,633"/>
    <polygon class="red-band" points="0,263 351,263 264,383 366,493 0,493"/>

    <rect class="brand-square" x="119" y="92" width="48" height="48"/>
    <text class="brand-name" x="143" y="210" text-anchor="middle" font-size="36" letter-spacing="3">TKRV</text>
    <text class="brand-sub" x="143" y="226" text-anchor="middle" font-size="7.5" letter-spacing="10">GROUP</text>

    <text class="headline" x="143" y="358" text-anchor="middle" font-size="95" letter-spacing="-3">TOP</text>
    <text class="headline" x="143" y="411" text-anchor="middle" font-size="46">QUALITY</text>
    <text class="headline" x="143" y="448" text-anchor="middle" font-size="32">RESTAURANT</text>
    <text class="headline headline--small" x="143" y="471" text-anchor="middle" font-size="17">MANAGEMENT</text>

    <text class="tagline" x="46" y="555" font-size="18" letter-spacing="0.5">WITH YEARS OF EXPERIENCE</text>
    <text class="tagline" x="46" y="575" font-size="18" letter-spacing="0.5">AND EXCELLENCE</text>

    <g class="venue--lark">
      <rect x="159" y="624" width="18" height="18"/>
      <text class="venue-name" x="168" y="666" text-anchor="middle" font-size="14">THE LARK</text>
      <text class="venue-line" x="168" y="676" text-anchor="middle" font-size="6">WHISKEY &amp; COFFEE</text>
    </g>
    <g class="venue--lantern">
      <circle cx="298" cy="633" r="9"/>
      <text class="venue-name" x="298" y="660" text-anchor="middle" font-size="13">JADE LANTERN</text>
      <text class="venue-line" x="298" y="670" text-anchor="middle" font-size="5">BAYVIEW | ELMWOOD | STONE RIDGE</text>
      <text class="venue-line" x="298" y="685" text-anchor="middle" font-size="5">JADELANTERNDINING.COM</text>
    </g>
    <g class="venue--harbor">
      <circle cx="446" cy="633" r="9"/>
      <text class="venue-name" x="446" y="664" text-anchor="middle" font-size="17">HARBOR</text>
      <text class="venue-line" x="446" y="674" text-anchor="middle" font-size="6.5" letter-spacing="3">PETE'S</text>
    </g>
  </svg>

</main>
</body>
</html>
```